Broschüre für Trainer für Resilienz
Zielgruppe
Wir sind ein Zusammenschluss von zwei selbstständigen Trainern, welche sich spezialisiert haben auf den Bereich Resilienz in Unternehmen.
Insgesamt haben wir hierfür 4 Säulen erarbeitet:
1. Resilienz - Training
2. Psychologische Beratung
3. Burnout - Prophylaxe
4. Weiterbildungen
Weitere Informationen finden Sie in der angehängten Datei mit dem Titel 'flyer_Inhalt'.
Als Zielgruppe haben wir mittelständische und große Unternehmen im Blick, hierbei jeweils die Mitarbeiter und Führungskräfte
Aufgabenstellung
Wir stellen uns eine Broschüre im DIN-A4 - Format vor, 6 Seiten mit Wickelfalz.
Eine Broschüre, welche bei Kunden großen Anklang gefunden hat, war meine Dozent4.1 - Broschüre, welche ich als Beispiel ebenfalls hochgeladen habe.
Nach ein paar Missverständnissen möchte ich das Format an dieser Stelle genauer beschreiben:
Es geht um einen Flyer/ eine Broschüre, welche im DIN-A4-Format gestaltet wird. Hierbei nicht ein DIN-A4-Format im Querformat, sondern DREI DIN-A4-Seiten, welche mit einer Wickelfalz verbunden sind und somit 6 DIN-A4-Flächen zum Bedrucken bilden.

```html
<!DOCTYPE html>
<html lang="de">
<head>
<meta charset="utf-8">
<title>Resilienz Broschüre – Innenseiten</title>
<link href="https://fonts.googleapis.com/css2?family=Open+Sans:wght@300;400;600;700&display=swap" rel="stylesheet">
<style>
  :root{
    --blue:#1f4a8c;
    --text:#3f444a;
    --rule:#a9adb2;
    --shield:#b3b6ba;
    --frame:#c5c7ca;
    --paper:#ffffff;
  }
  *{margin:0;padding:0;box-sizing:border-box}
  html,body{width:1200px;height:566px;overflow:hidden;background:var(--paper)}
  body{position:relative;font-family:"Open Sans",Arial,sans-serif;color:var(--text)}

  .photo{position:absolute}
  .photo-stress{left:0;top:38px;width:402px;height:263px;
    background:linear-gradient(120deg,#d9dde2 0%,#eceef0 40%,#c9ccd0 70%,#9ea3a8 100%)}
  .photo-team{left:403px;top:358px;width:401px;height:208px;
    background:linear-gradient(160deg,#c8cacc 0%,#8a8f98 45%,#6c7280 70%,#b9b3ae 100%)}

  .cover-band{position:absolute;left:0;top:247px;width:267px;height:54px;background:rgba(255,255,255,.82)}
  .cover-title{position:absolute;left:28px;top:268px;font-size:22px;font-weight:400;color:var(--blue);letter-spacing:-.2px;white-space:nowrap}
  .cover-title strong{font-weight:700}

  .intro{position:absolute;left:107px;top:318px;border-left:1px dotted var(--rule);padding-left:7px;font-size:7.8px;line-height:10.2px;font-weight:400;white-space:nowrap}
  .intro p{margin-bottom:8px}

  .section h2{position:absolute;font-weight:300;font-size:23px;color:var(--blue);white-space:nowrap;letter-spacing:-.2px}
  .section .body{position:absolute;border-left:1px dotted var(--rule);padding-left:7px;font-size:7.8px;line-height:12.2px;font-weight:400;white-space:nowrap}
  .section .body p{margin-bottom:9.5px}
  .section .body p:last-child{margin-bottom:0}
  .section svg.shield{position:absolute;width:12px;height:14px}

  .wordcloud{position:absolute;left:923px;top:327px;width:221px;height:204px;border:1px solid var(--frame);background:var(--paper)}
  .wordcloud-art{position:absolute;left:8px;top:8px;right:8px;height:130px;
    background:radial-gradient(ellipse at 55% 55%,#6f7fb8 0%,#a9b6d8 40%,#e6dcbc 70%,#ffffff 100%)}
</style>
</head>
<body>

  <div class="photo photo-stress" role="img" aria-label="Foto: gestresste Mitarbeiterin am Schreibtisch, umringt von Händen mit Papieren und Telefonen"></div>
  <div class="cover-band"></div>
  <div class="cover-title"><strong>Stärken</strong> Sie Ihr Team.</div>

  <div class="intro">
    <p>Der Mitarbeiter von heute wird mit<br>hohen Leistungsanforderungen konfrontiert.</p>
    <p>Häufig Reaktionen hierbei sind Überforderung, Stress,<br>Angst zu Versagen und Burnout.</p>
    <p>Aus Sicht von Unternehmen bedeutet dies eine<br>verminderte Leistungsfähigkeit des Teams, erhöhte Anzahl an<br>Krankheitstagen, unkalkulierbare Mehrkosten und nicht zuletzt<br>einer Verminderung der Wettbewerbsfähigkeit.</p>
    <p>Die betriebliche Gesundheitsförderung findet hierbei<br>immer mehr Anklang und wird vom Gesetzgeber gefördert.</p>
    <p>Lernen Sie, wie die betriebliche Gesundheitsförderung mit<br>wenig Aufwand, Teil Ihres Unternehmens werden kann!</p>
  </div>

  <section class="section">
    <h2 style="left:457px;top:46px">Resilienz-Training</h2>
    <svg class="shield" style="left:490px;top:84px" viewBox="0 0 12 14"><path d="M6 0 L12 2 V7 C12 10 9 12.5 6 14 C3 12.5 0 10 0 7 V2 Z" fill="var(--shield)"/></svg>
    <div class="body" style="left:509px;top:82px">
      <p>Ihre Mitarbeiter verfügen über genügend eigene Ressourcen,<br>um die Anforderungen eines Arbeitsalltags zu bewältigen.<br>Diese psychische Widerstandskraft kann von Zeit zu Zeit<br>Schwankungen unterliegen.</p>
      <p>Leicht zu erlernende Methoden, wie Stress- und Selbst-<br>management oder Entspannung helfen Ihren Mitarbeitern,<br>ihr Gleichgewicht wieder zu finden.</p>
    </div>
  </section>

  <section class="section">
    <h2 style="left:457px;top:199px">Psychische Beratung</h2>
    <svg class="shield" style="left:490px;top:238px" viewBox="0 0 12 14"><path d="M6 0 L12 2 V7 C12 10 9 12.5 6 14 C3 12.5 0 10 0 7 V2 Z" fill="var(--shield)"/></svg>
    <div class="body" style="left:509px;top:237px">
      <p>Die psychische Beratung gliedert sich in eine individuelle<br>psychische Diagnostik und umfangreiche Beratung.</p>
      <p>Emotionale, persönliche und berufliche Probleme können in<br>der Beratung thematisiert werden, um individuelle Lösungen<br>zu erarbeiten.</p>
      <p>Den eigenen Weg zur Kraft und Ausdauer zu finden ist hierbei<br>das übergeordnete Ziel.</p>
    </div>
  </section>

  <div class="photo photo-team" role="img" aria-label="Foto: fröhliche Gruppe von Geschäftsleuten, von oben fotografiert, mit erhobenen Daumen"></div>

  <section class="section">
    <h2 style="left:860px;top:46px">Burnout-Prophylaxe</h2>
    <svg class="shield" style="left:892px;top:84px" viewBox="0 0 12 14"><path d="M6 0 L12 2 V7 C12 10 9 12.5 6 14 C3 12.5 0 10 0 7 V2 Z" fill="var(--shield)"/></svg>
    <div class="body" style="left:911px;top:82px">
      <p>Hohe Leistungsanforderungen und individuelle Persönlich-<br>keitsmerkmale bilden die Grundlage für eine erhöhte Burnout-<br>Gefährdung. Diese Abwärts-Spirale selbst zu erkennen ist<br>beinahe unmöglich und bildet die Basis für eine stetige<br>Verschlechterung der Leistungsfähigkeit.</p>
      <p>Die eigene Gefährdung mit Hilfe eines „Ampel-Systems“<br>zu erkennen ist Ziel der Burnout-Prophylaxe. Entsprechende<br>Methoden werden dem Teilnehmer aufgezeigt , um diesen<br>Kreislauf zu durchbrechen und neue Kraft und Stärke zu<br>gewinnen.</p>
    </div>
  </section>

  <section class="section">
    <h2 style="left:860px;top:239px">Weiterbildungen</h2>
    <svg class="shield" style="left:892px;top:277px" viewBox="0 0 12 14"><path d="M6 0 L12 2 V7 C12 10 9 12.5 6 14 C3 12.5 0 10 0 7 V2 Z" fill="var(--shield)"/></svg>
    <div class="body" style="left:911px;top:275px">
      <p>Weiterbildungen als Synthese von klinischer Psychologie<br>und Training.</p>
    </div>
  </section>

  <div class="wordcloud">
    <div class="wordcloud-art" role="img" aria-label="Grafik: Schlagwortwolke rund um Stress, Burnout, Resilienz und Entspannungsmethoden"></div>
  </div>

</body>
</html>
```